Business Card Design Can you design a business card design? Looking for something unique and differe

Can you design a business card design? Looking for something unique and different. Can you design a business card design? Looking for something unique and different.Can you design a business card design? Looking for something unique and different.Can you design a business card design? Looking for something unique and different.Can you design a business card design? Looking for something unique and different.Can you design a business card design? Looking for something unique and different.

Industry/Entity Type

Business

Contact Information for Business Card

Can you design a business card design? Looking for something unique and different.

Font styles to use
Serif

```html
<!DOCTYPE html>
<html lang="en">
<head>
<meta charset="utf-8">
<title>Medwise Rx Costs — Business Card</title>
<link href="https://fonts.googleapis.com/css2?family=Lato:wght@400;700&display=swap" rel="stylesheet">
<style>
  :root {
    --page-bg: #ece8ef;
    --purple-deep: #74468e;
    --purple-mid: #9a78b0;
    --purple-band: #9b7bad;
    --purple-text: #7a5490;
    --grey-mark: #8a8a8a;
    --white: #ffffff;
    --white-soft: #f3f3f3;
    --shadow: rgba(40, 20, 50, 0.22);
  }
  * { box-sizing: border-box; margin: 0; padding: 0; }
  html, body { width: 1200px; height: 900px; overflow: hidden; }
  body {
    background: var(--page-bg);
    font-family: "Lato", Arial, sans-serif;
    position: relative;
  }
  .card {
    position: absolute;
    width: 588px;
    height: 336px;
    border-radius: 4px;
    box-shadow: 0 14px 30px var(--shadow);
    overflow: hidden;
  }
  /* Front */
  .card-front {
    left: 110px;
    top: 90px;
    background: radial-gradient(ellipse at 55% 40%, var(--purple-mid) 0%, var(--purple-deep) 100%);
    display: flex;
    align-items: center;
    justify-content: center;
  }
  .brand {
    display: flex;
    align-items: center;
    gap: 14px;
    font-weight: 700;
    letter-spacing: 0.5px;
  }
  .brand-square {
    width: 26px;
    height: 26px;
    border-radius: 3px;
  }
  .card-front .brand { color: var(--white); font-size: 40px; }
  .card-front .brand-square { background: var(--white); }

  /* Back */
  .card-back {
    left: 500px;
    top: 470px;
    background: var(--purple-band);
  }
  .back-top {
    height: 156px;
    background: linear-gradient(180deg, var(--white) 0%, var(--white-soft) 100%);
    display: flex;
    align-items: center;
    justify-content: center;
  }
  .card-back .brand { color: var(--purple-text); font-size: 36px; }
  .card-back .brand-square { background: var(--grey-mark); }
  .back-details {
    display: flex;
    justify-content: space-between;
    padding: 30px 40px 0 40px;
    color: var(--white);
  }
  .person { text-align: right; }
  .person-name { font-size: 25px; font-weight: 400; line-height: 1.1; }
  .person-role { font-size: 17px; margin-top: 4px; }
  .person-address { font-size: 19px; margin-top: 14px; line-height: 1.25; }
  .contacts { list-style: none; font-size: 16px; }
  .contacts li {
    display: flex;
    align-items: center;
    gap: 9px;
    margin-bottom: 7px;
  }
  .contact-icon {
    width: 18px;
    height: 18px;
    flex: none;
  }
</style>
</head>
<body>

  <section class="card card-front" aria-label="Business card front">
    <div class="brand">
      <span class="brand-square"></span>
      <span class="brand-name">Medwise Rx Costs</span>
    </div>
  </section>

  <section class="card card-back" aria-label="Business card back">
    <div class="back-top">
      <div class="brand">
        <span class="brand-square"></span>
        <span class="brand-name">Medwise Rx Costs</span>
      </div>
    </div>
    <div class="back-details">
      <div class="person">
        <p class="person-name">Daniel Reyes</p>
        <p class="person-role">Managing Director</p>
        <p class="person-address">48 Harbor Lane<br>Riverton, 40512</p>
      </div>
      <ul class="contacts">
        <li>
          <svg class="contact-icon" viewBox="0 0 18 18" aria-hidden="true">
            <rect width="18" height="18" rx="3" fill="#fff"/>
            <path d="M5 4.5c.8-.6 1.5-.3 1.9.4l.8 1.4c.3.6 0 1.1-.5 1.4l-.5.3c.5 1.3 1.6 2.4 2.9 2.9l.3-.5c.3-.5.8-.8 1.4-.5l1.4.8c.7.4 1 1.1.4 1.9-.7.9-1.8 1.2-3 .7C7.6 12.3 5.7 10.4 4.8 7.9c-.5-1.2-.2-2.6.2-3.4z" fill="var(--purple-band)"/>
          </svg>
          <span>555-014-2270</span>
        </li>
        <li>
          <svg class="contact-icon" viewBox="0 0 18 18" aria-hidden="true">
            <rect width="18" height="18" rx="3" fill="#fff"/>
            <rect x="4" y="4" width="10" height="10" rx="1.5" fill="none" stroke="var(--purple-band)" stroke-width="1.6"/>
            <path d="M6 7h6M6 9.5h6M6 12h4" stroke="var(--purple-band)" stroke-width="1.3"/>
          </svg>
          <span>555-014-2271</span>
        </li>
        <li>
          <svg class="contact-icon" viewBox="0 0 18 18" aria-hidden="true">
            <rect width="18" height="18" rx="3" fill="#fff"/>
            <rect x="3.5" y="5" width="11" height="8" rx="1" fill="none" stroke="var(--purple-band)" stroke-width="1.5"/>
            <path d="M3.8 5.5 9 9.6l5.2-4.1" fill="none" stroke="var(--purple-band)" stroke-width="1.5"/>
          </svg>
          <span>info@medwiserx.com</span>
        </li>
        <li>
          <svg class="contact-icon" viewBox="0 0 18 18" aria-hidden="true">
            <rect width="18" height="18" rx="3" fill="#fff"/>
            <path d="M7.5 10.5 10.5 7.5M8.2 5.6l1-1a2.3 2.3 0 0 1 3.2 3.2l-1 1M9.8 12.4l-1 1a2.3 2.3 0 0 1-3.2-3.2l1-1" fill="none" stroke="var(--purple-band)" stroke-width="1.5" stroke-linecap="round"/>
          </svg>
          <span>www.medwiserx.com</span>
        </li>
      </ul>
    </div>
  </section>

</body>
</html>
```